Travel Blogger Business Card for roamquill.net

I need a two-sided business card for a travel blogging website. The card should be both professional and fun at the same time. This is for the website www.roamquill.net

I don't necessarily think that the current logo on the website needs to be used on the business card but it can be. I am very flexible with ideas

Target Market(s)

Travel agencies that will be met at a conference.

Industry/Entity Type

Travel

Contact Information for Business Card

Company Name: Roam Quill.net
Name: Bertrand Olesky
Voice: +1-(345)-402-7731
Address: Coral Reach Shore, Grand Cayman, Cayman Islands
Email: ceo@roamquill.net

Colors
0592cd
0355a3
3176b5
33a6d7
85cae6
85acd3

Requirements
Must have
• Website address and name should be bigger than address, phone number, and email.

```html
<!DOCTYPE html>
<html lang="en">
<head>
<meta charset="utf-8">
<title>Roam Quill.net – Business Card</title>
<link rel="stylesheet" href="https://fonts.googleapis.com/css2?family=Questrial&family=Roboto:wght@700&display=swap">
<style>
  :root {
    --page: #ffffff;
    --front-deep: #0f3444;
    --front-mid: #1a4a5c;
    --front-dark: #0b2632;
    --ink: #1b4658;
    --silhouette-dark: #050708;
    --back-paper: #f3f3f3;
    --back-map: #e2e2e2;
    --white: #ffffff;
  }
  * { box-sizing: border-box; margin: 0; padding: 0; }
  html, body {
    width: 1053px; height: 1200px; overflow: hidden;
    background: var(--page);
  }
  .sheet { position: relative; width: 1053px; height: 1200px; }

  .card {
    position: absolute;
    width: 766px; height: 438px;
    left: 119px;
    overflow: hidden;
    box-shadow: 0 6px 14px rgba(0,0,0,0.35);
  }
  .card--front { top: 103px; }
  .card--back  { top: 612px; left: 121px; width: 764px; height: 439px; }

  /* backgrounds standing in for the antique world map */
  .map-fill { position: absolute; inset: 0; }
  .card--front .map-fill {
    background: radial-gradient(ellipse at 55% 40%, var(--front-mid) 0%, var(--front-deep) 60%, var(--front-dark) 100%);
  }
  .card--back .map-fill {
    background: radial-gradient(ellipse at 50% 45%, var(--back-paper) 0%, var(--back-map) 100%);
  }

  /* band standing in for the landmark skyline */
  .skyline {
    position: absolute; left: 0; right: 0; bottom: 0;
    height: 105px;
  }
  .card--front .skyline {
    background: linear-gradient(to bottom, rgba(5,7,8,0) 0%, rgba(5,7,8,0.7) 45%, var(--silhouette-dark) 75%);
  }
  .card--back .skyline {
    background: linear-gradient(to bottom, rgba(27,70,88,0) 0%, rgba(27,70,88,0.75) 45%, var(--ink) 75%);
  }

  /* front */
  .brand {
    position: absolute; left: 0; right: 0; top: 176px;
    display: flex; align-items: center; justify-content: center; gap: 14px;
    padding-right: 20px;
  }
  .brand__dot {
    width: 44px; height: 44px; border-radius: 50%;
    background: var(--white);
  }
  .brand__name {
    font-family: "Roboto", Arial, sans-serif;
    font-weight: 700; font-size: 50px; line-height: 1;
    color: var(--white); letter-spacing: 0.5px;
  }
  .front-url {
    position: absolute; left: 0; right: 0; top: 232px;
    text-align: center;
    font-family: "Questrial", Arial, sans-serif;
    font-size: 26px; line-height: 1;
    letter-spacing: 11px;
    color: var(--white);
  }

  /* back */
  .holder {
    position: absolute; left: 0; right: 0; top: 34px;
    text-align: center;
    font-family: "Questrial", Arial, sans-serif;
    font-size: 66px; line-height: 1;
    color: var(--ink); letter-spacing: 1px;
  }
  .contact {
    position: absolute; left: 0; right: 0;
    display: flex; align-items: flex-start; justify-content: center; gap: 12px;
    font-family: "Questrial", Arial, sans-serif;
    font-size: 21px; line-height: 26px;
    color: var(--ink); letter-spacing: 0.5px;
  }
  .contact svg { flex: none; fill: var(--ink); }
  .contact__text { text-align: center; }
  .contact--phone   { top: 122px; }
  .contact--address { top: 166px; }
  .contact--email   { top: 230px; }
  .contact--web     { top: 284px; }
</style>
</head>
<body>
<main class="sheet">

  <section class="card card--front">
    <div class="map-fill" role="img" aria-label="Dark teal antique world map texture"></div>
    <div class="skyline" role="img" aria-label="Black silhouette skyline of world landmarks"></div>
    <div class="brand">
      <span class="brand__dot"></span>
      <span class="brand__name">ROAM QUILL</span>
    </div>
    <p class="front-url">www.Roamquill.net</p>
  </section>

  <section class="card card--back">
    <div class="map-fill" role="img" aria-label="Faint grey antique world map texture"></div>
    <div class="skyline" role="img" aria-label="Teal silhouette skyline of world landmarks"></div>

    <h1 class="holder">Bertrand Olesky</h1>

    <div class="contact contact--phone">
      <svg width="16" height="28" viewBox="0 0 16 28" aria-hidden="true">
        <path d="M3 0h10a3 3 0 0 1 3 3v22a3 3 0 0 1-3 3H3a3 3 0 0 1-3-3V3a3 3 0 0 1 3-3zm-1 4v18h12V4zm6 19.5a1.5 1.5 0 1 0 0 3 1.5 1.5 0 0 0 0-3z"/>
      </svg>
      <span class="contact__text">+1-(345)-402-7731</span>
    </div>

    <div class="contact contact--address">
      <svg width="20" height="28" viewBox="0 0 20 28" aria-hidden="true">
        <path d="M10 0a10 10 0 0 1 10 10c0 7-10 18-10 18S0 17 0 10A10 10 0 0 1 10 0zm0 6a4 4 0 1 0 0 8 4 4 0 0 0 0-8z"/>
      </svg>
      <span class="contact__text">Coral Reach Shore, Grand Cayman,<br>Cayman Islands.</span>
    </div>

    <div class="contact contact--email">
      <svg width="28" height="26" viewBox="0 0 28 26" aria-hidden="true">
        <path d="M0 7h28v3L14 17 0 10zm0 6l14 7 14-7v10H0z"/>
      </svg>
      <span class="contact__text">ceo@roamquill.net</span>
    </div>

    <div class="contact contact--web">
      <svg width="28" height="28" viewBox="0 0 28 28" aria-hidden="true">
        <g fill="none" stroke="#1b4658" stroke-width="2">
          <circle cx="14" cy="14" r="12"/>
          <ellipse cx="14" cy="14" rx="5.5" ry="12"/>
          <path d="M2 14h24M4 8h20M4 20h20M14 2v24"/>
        </g>
      </svg>
      <span class="contact__text">www.roamquill.net</span>
    </div>
  </section>

</main>
</body>
</html>
```